"Harrow Crest Builders" is a residential building company and needs a new business card design and may re

We would like a redesign based on the existing logo, and would like to see a new font as well. We are bespoke home builders who build sustainable energy efficient homes.

Industry/Entity Type

Construction

Contact Information for Business Card

Business card size 40mm x 90mm

Colors

Designer to choose colors to be used in the design.

```html
<!DOCTYPE html>
<html lang="en">
<head>
<meta charset="utf-8">
<title>Harrow Crest Builders – Business Card</title>
<link rel="stylesheet" href="https://fonts.googleapis.com/css2?family=Montserrat:wght@400;600;700&family=Quicksand:wght@400;500&display=swap">
<style>
  :root {
    --stage: #2a2a2c;
    --card-dark: #232325;
    --card-light: #ffffff;
    --navy: #27408b;
    --orange: #f07a1a;
    --grey-text: #6b6b70;
    --ink: #333338;
  }
  * { box-sizing: border-box; margin: 0; padding: 0; }
  html, body { width: 1200px; height: 900px; overflow: hidden; }
  body {
    background: var(--stage);
    font-family: "Quicksand", sans-serif;
    position: relative;
  }
  .card {
    position: absolute;
    left: 240px;
    width: 720px;
    height: 400px;
    border-radius: 4px;
    box-shadow: 0 10px 30px rgba(0,0,0,0.45);
    overflow: hidden;
  }
  .card--front { top: 36px; background: linear-gradient(135deg, #1e1e20 0%, #2e2e31 100%); }
  .card--back { top: 464px; background: var(--card-light); }

  .brand { display: flex; align-items: center; gap: 18px; position: absolute; }
  .brand__mark { width: 42px; height: 42px; background: var(--orange); }
  .brand__name {
    font-family: "Montserrat", sans-serif;
    font-weight: 600;
    color: var(--navy);
    line-height: 1.1;
    letter-spacing: 0.06em;
    text-transform: uppercase;
  }
  .card--front .brand { left: 50%; top: 50%; transform: translate(-50%, -50%); }
  .card--front .brand__name { font-size: 30px; color: #3a5bb8; }
  .card--back .brand { right: 44px; top: 60px; }
  .card--back .brand__name { font-size: 26px; }
  .brand__sub { display: block; font-size: 0.62em; letter-spacing: 0.42em; }

  .holder { position: absolute; left: 48px; top: 206px; }
  .holder__name {
    font-family: "Montserrat", sans-serif;
    font-weight: 700;
    font-size: 21px;
    color: var(--navy);
    letter-spacing: 0.02em;
  }
  .holder__role { font-size: 16px; color: var(--ink); margin-top: 2px; font-weight: 500; }

  .divider {
    position: absolute; left: 44px; right: 44px; top: 272px;
    height: 2px; background: var(--orange);
  }

  .contacts { position: absolute; left: 48px; top: 290px; list-style: none; }
  .contacts li {
    display: flex; align-items: center; gap: 12px;
    font-size: 16px; color: var(--grey-text); line-height: 27px;
  }
  .contacts svg { width: 14px; height: 14px; fill: none; stroke: var(--orange); stroke-width: 2; }

  .address {
    position: absolute; right: 44px; top: 290px;
    text-align: right; font-size: 16px; color: var(--grey-text); line-height: 27px;
  }
  .address .label { color: var(--navy); font-weight: 500; }
</style>
</head>
<body>
  <section class="card card--front">
    <div class="brand">
      <span class="brand__mark"></span>
      <span class="brand__name">Harrow Crest<span class="brand__sub">builders</span></span>
    </div>
  </section>

  <section class="card card--back">
    <div class="brand">
      <span class="brand__mark"></span>
      <span class="brand__name">Harrow Crest<span class="brand__sub">builders</span></span>
    </div>

    <div class="holder">
      <h1 class="holder__name">DANIEL MORROW</h1>
      <p class="holder__role">Founder</p>
    </div>

    <div class="divider"></div>

    <ul class="contacts">
      <li>
        <svg viewBox="0 0 16 16"><path d="M4 2l2.5 3-1.5 2a8 8 0 0 0 4 4l2-1.5 3 2.5-1.5 2C7 14 2 9 2 3.5z"/></svg>
        0400 555 019
      </li>
      <li>
        <svg viewBox="0 0 16 16"><rect x="2" y="4" width="12" height="9"/><path d="M2 4l6 5 6-5"/></svg>
        daniel@harrowcrest.com.au
      </li>
      <li>
        <svg viewBox="0 0 16 16"><circle cx="8" cy="8" r="6"/><path d="M2 8h12M8 2c-3 3-3 9 0 12M8 2c3 3 3 9 0 12"/></svg>
        www.harrowcrest.com.au
      </li>
    </ul>

    <div class="address">
      <p>PO Box 2140 Eastgate</p>
      <p>LPO Ridgeview WA 6099</p>
      <p><span class="label">Reg:</span> -40873 | <span class="label">ABN:</span> 52 304 618 775</p>
    </div>
  </section>
</body>
</html>
```